Create our new Brightcup Coffee Syrup Label designs. A delicious job!

Design a front label for a range of coffee syrup flavours. The brand is 'Brightcup Coffee Syrups'. The flavours, vanilla, hazelnut and caramel.
Our coffee syrups are made with only natural colours and flavours and are positioned in the popular premium space in Australian and international cafes.
The labels will be applied to 750 ml Boston Bottles (see attached image).
Given that coffee syrups are often positioned in high visibility locations in cafes, they can be considered as objects of functional beauty.
This range is a sub brand for our company and I have attached our main brand images in the flavours we want. we want this brand to look different to this Marlowe branded range, but included the image to show what we are currently doing in this space.
The different flavours can be identified by a combination of colour and text, which may be a line or section of the otherwise same overall design.
We are going to do a 2 part label with the front just carrying Brand and flavour descriptors plus 750 ml.
Total Bottle height is 240 mm bottle width is 70 mm

Target Market(s)

Cafe patrons, primarily women, 18-35, Middle class in terms of economics, regular cafe patrons. Who are looking for a guilt free treat in their busy day.

Logo Text

Brightcup Coffee Syrups Vanilla (or Hazelnut, or Caramel) 750 ml

Logo styles of interest
Pictorial/Combination Logo
Font styles to use
Sans Serif

Colors

Designer to choose colors to be used in the design.

Requirements
Must have
• A clear design, which is a combination of font and image. it needs to be legible from up to 2m away (across a counter in a cafe).
• We would like to see a device, which may be a gold drop, that may be the 'brightcup' meant to the coffee.
• The way our coffee syrups are used is by adding a small amount (15 ml) to a cup
• of coffee, this adds both flavour and sweetness to the overall coffee experience, and cafes charge a premium for this service. We want our package to show this will be a great thing to do.
• We have a few options in terms of Label stock. We can print on a foil, that will allow a metallic sheen to come through the colours (see example of the Marlowe branded bottles.
Nice to have
• We are looking for a modern, clean and distinctive look and feel to this range.
• I have added a key line for the front and back label, however we can create a different label die line should the design warrant that. Note this is just for the front label.
Should not have
• Difficult to read fonts or imagery that is not clear.
• Should look different to the Marlowe branded product range.

```html
<!DOCTYPE html>
<html lang="en">
<head>
<meta charset="utf-8">
<title>Brightcup Coffee Syrups — Front Labels</title>
<link rel="stylesheet" href="https://fonts.googleapis.com/css2?family=Josefin+Sans:wght@600&family=Courgette&family=Roboto+Condensed:wght@400;500&display=swap">
<style>
  :root {
    --page: #ffffff;
    --caramel-bg: #c4581f;
    --caramel-edge: #3a56a8;
    --caramel-drop: #3a56a8;
    --vanilla-bg: #173f45;
    --vanilla-edge: #efdfa2;
    --vanilla-drop: #1fb3a8;
    --hazelnut-bg: #b8174a;
    --hazelnut-edge: #8cc43c;
    --hazelnut-drop: #8cc43c;
    --brand-cream: #f7e3a0;
    --subline-teal: #74bcae;
    --flavour-white: #ffffff;
    --volume-grey: #8fb3ad;
  }
  * { margin: 0; padding: 0; box-sizing: border-box; }
  html, body {
    width: 1200px;
    height: 1000px;
    overflow: hidden;
    background: var(--page);
  }
  .canvas {
    position: relative;
    width: 1200px;
    height: 1000px;
  }
  .label {
    position: absolute;
    top: 312px;
    width: 240px;
    height: 376px;
    border: 3px solid;
    border-radius: 7px;
    display: flex;
    flex-direction: column;
    align-items: center;
  }
  .label--caramel  { left: 173px; background: var(--caramel-bg);  border-color: var(--caramel-edge); }
  .label--vanilla  { left: 481px; background: var(--vanilla-bg);  border-color: var(--vanilla-edge); }
  .label--hazelnut { left: 790px; background: var(--hazelnut-bg); border-color: var(--hazelnut-edge); }

  .label__mark {
    margin-top: 28px;
    width: 110px;
    height: 150px;
  }
  .label__brand {
    margin-top: 20px;
    font-family: "Josefin Sans", sans-serif;
    font-weight: 600;
    font-size: 34px;
    line-height: 1;
    color: var(--brand-cream);
    letter-spacing: 0.5px;
  }
  .label__subline {
    margin-top: 4px;
    font-family: "Roboto Condensed", sans-serif;
    font-weight: 500;
    font-size: 11px;
    letter-spacing: 3px;
    color: var(--subline-teal);
  }
  .label__dot {
    margin-top: 9px;
    width: 4px;
    height: 4px;
    border-radius: 50%;
    background: var(--flavour-white);
  }
  .label__flavour {
    margin-top: 8px;
    font-family: "Courgette", cursive;
    font-size: 27px;
    line-height: 1.1;
    color: var(--flavour-white);
  }
  .label__volume {
    margin-top: 6px;
    font-family: "Roboto Condensed", sans-serif;
    font-size: 10px;
    letter-spacing: 0.5px;
    color: var(--volume-grey);
  }
</style>
</head>
<body>
<main class="canvas">

  <section class="label label--caramel">
    <svg class="label__mark" viewBox="0 0 110 150" role="img" aria-label="Brand device: patterned drop in blue">
      <circle cx="55" cy="90" r="52" fill="var(--caramel-drop)"/>
    </svg>
    <p class="label__brand">brightcup</p>
    <p class="label__subline">COFFEE SYRUPS</p>
    <span class="label__dot"></span>
    <h2 class="label__flavour">Caramel</h2>
    <p class="label__volume">750ML</p>
  </section>

  <section class="label label--vanilla">
    <svg class="label__mark" viewBox="0 0 110 150" role="img" aria-label="Brand device: floral patterned drop in turquoise">
      <circle cx="55" cy="90" r="52" fill="var(--vanilla-drop)"/>
    </svg>
    <p class="label__brand">brightcup</p>
    <p class="label__subline">COFFEE SYRUPS</p>
    <span class="label__dot"></span>
    <h2 class="label__flavour">Vanilla</h2>
    <p class="label__volume">750ML</p>
  </section>

  <section class="label label--hazelnut">
    <svg class="label__mark" viewBox="0 0 110 150" role="img" aria-label="Brand device: leaf patterned drop in green">
      <circle cx="55" cy="90" r="52" fill="var(--hazelnut-drop)"/>
    </svg>
    <p class="label__brand">brightcup</p>
    <p class="label__subline">COFFEE SYRUPS</p>
    <span class="label__dot"></span>
    <h2 class="label__flavour">Hazelnut</h2>
    <p class="label__volume">750ML</p>
  </section>

</main>
</body>
</html>
```